Restaurant Bar website in Oakland

Landing page that looks good on mobile and home. Easy to make changes to SEO and Menu page .
Might link with online ordering through the point of sale provider or not. Either way we want to be able to upload menus.
No forms need. Just landing page, about page with a paragraph and a few photos, address, hours and a mailto info@
A press page and an faq

Target Market(s)

Customers

Coding

Coded - Design and coding required

Number of Pages Required

4 page

Colors
00a990
ffc214

Requirements
Must have
• Simple to scroll
SEO
Simple to add menus
Our logo

```html
<!DOCTYPE html>
<html lang="en">
<head>
<meta charset="utf-8">
<title>Marlow's — Restaurant & Bar</title>
<link href="https://fonts.googleapis.com/css2?family=Bebas+Neue&family=Lato:wght@400;700&display=swap" rel="stylesheet">
<style>
:root{
  --teal:#00a990;
  --gold:#ffc214;
  --amber:#e3a73f;
  --line:#d9a53a;
  --ink:#1d1d1d;
  --body:#555;
  --dark:#222;
  --forest:#2c4b35;
  --price:#e3a73f;
}
*{margin:0;padding:0;box-sizing:border-box}
html,body{width:1200px;height:5259px;overflow:hidden}
body{position:relative;font-family:'Lato',sans-serif;color:var(--body);background:#fff}
.abs{position:absolute}
.display{font-family:'Bebas Neue',sans-serif;color:var(--ink);letter-spacing:1px;font-weight:400}
.btn{position:absolute;display:flex;align-items:center;justify-content:center;font-size:13px;font-weight:700;color:#fff;background:var(--teal);text-transform:uppercase;letter-spacing:.5px}
.rule{position:absolute;height:2px;background:var(--line)}
p.copy{font-size:12.5px;line-height:22px;color:var(--body)}

/* hero */
.hero-photo{left:0;top:0;width:1200px;height:790px;background:radial-gradient(ellipse at 50% 55%,#6b4a2a 0%,#3b2a1c 45%,#1a130e 100%)}
.hero-curve{left:0;top:560px}
.frame-h{left:0;top:113px;width:1200px;height:1px;background:var(--line)}
.frame-v{top:0;width:1px;height:620px;background:var(--line)}
.brand-mark{left:110px;top:18px;display:flex;align-items:center;gap:8px}
.brand-mark .dot{width:14px;height:14px;border-radius:50%;background:var(--gold)}
.brand-mark span{font-family:'Bebas Neue',sans-serif;font-size:28px;color:var(--gold);letter-spacing:1px}
.nav{left:370px;top:56px;display:flex;gap:40px;font-size:13px;color:#fff}
.nav .on{color:var(--gold)}
.cart{left:1068px;top:50px}
.hero-title{left:0;top:352px;width:1200px;text-align:center;font-size:66px;color:#fff}
.hero-text{left:290px;top:432px;width:620px;text-align:center;font-size:13px;line-height:26px;color:#fff}
.hero-btn{left:516px;top:512px;width:162px;height:44px;background:var(--gold);color:#222;font-weight:400}

/* features */
.feature .icon{width:52px;height:52px;border-radius:50%;background:var(--gold)}
.feature h3{font-size:28px;margin:14px 0 8px}

/* cards */
.menu-img{width:290px;height:230px;border-radius:0 0 48px 0}
.menu-card h3{font-size:22px;margin:16px 0 8px 14px}
.menu-card p{margin-left:14px}
.menu-card .price{margin:12px 0 0 14px;font-size:15px;color:var(--price)}

.blog-card{background:#fff;box-shadow:0 4px 14px rgba(0,0,0,.12);width:313px;height:448px}
.blog-card .img{width:307px;height:220px;margin:3px}
.blog-card .meta{display:flex;justify-content:space-between;align-items:baseline;padding:20px 20px 0 20px}
.blog-card h3{font-size:22px}
.blog-card .date{font-size:12px;color:#555}
.blog-card p{padding:10px 20px 0 20px}
.blog-card a{display:block;padding:16px 20px 0;font-size:12px;color:var(--teal);text-decoration:underline}

/* faq */
.faq-item{position:absolute;left:110px;width:480px;height:34px;border:1px solid #e6e6e6;font-size:12px;color:#333;display:flex;align-items:center;padding:0 14px;justify-content:space-between}
.faq-item .tick{width:14px;height:14px;border-radius:50%;background:var(--teal)}
.faq-open{position:absolute;left:110px;top:4300px;width:480px;height:86px;border:1px solid #e6e6e6;padding:12px 14px}
.faq-open h4{font-size:13px;font-weight:700;color:#333}

/* footer */
.footer h4{font-family:'Bebas Neue',sans-serif;font-size:22px;color:#fff;letter-spacing:1px;font-weight:400}
.footer li{list-style:none;font-size:12px;color:#fff;line-height:27px}
.footer li b{color:var(--gold);font-weight:400;margin-right:10px}
.field{position:absolute;border:1px solid #fff;background:#fff;font-size:9px;color:#aaa;padding:6px}
.social{width:26px;height:26px;border-radius:50%}
</style>
</head>
<body>

<!-- Hero -->
<div class="abs hero-photo" role="img" aria-label="Restaurant table with wine glasses and plated dishes"></div>
<svg class="abs hero-curve" width="1200" height="240" viewBox="0 0 1200 240">
  <path d="M0 40 Q600 400 1200 40 L1200 240 L0 240 Z" fill="#fff"/>
  <path d="M0 40 Q600 400 1200 40" fill="none" stroke="#d9a53a" stroke-width="2"/>
</svg>
<div class="abs frame-h"></div>
<div class="abs frame-v" style="left:114px"></div>
<div class="abs frame-v" style="left:1085px"></div>
<div class="abs brand-mark"><div class="dot"></div><span>Marlow's</span></div>
<nav class="abs nav"><span class="on">Home</span><span>Abouts us</span><span>Menus</span><span>Press</span><span>FAQ's</span><span>Contact us</span></nav>
<svg class="abs cart" width="22" height="24" viewBox="0 0 22 24"><path d="M3 7h16l-1 15H4z M7 7V5a4 4 0 0 1 8 0v2" fill="none" stroke="#fff" stroke-width="1.6"/></svg>
<div class="rule" style="left:560px;top:330px;width:80px"></div>
<h1 class="abs display hero-title">Welcome to Marlow's</h1>
<p class="abs hero-text">Lorem Ipsum is simply dummy text of the printing and typesetting industry. Lorem Ipsum has been the industry's standard dummy text ever since the 1500s</p>
<div class="btn hero-btn">View Oue Menu</div>

<!-- Features -->
<div class="abs feature" style="left:115px;top:855px;width:260px"><div class="icon"></div><h3 class="display">Fresh Food</h3><p class="copy">Lorem Ipsum is simply dummy text of the printing and typesetting industry.</p></div>
<div class="abs feature" style="left:470px;top:855px;width:260px"><div class="icon"></div><h3 class="display">Good Wines</h3><p class="copy">Lorem Ipsum is simply dummy text of the printing and typesetting industry.</p></div>
<div class="abs feature" style="left:845px;top:855px;width:260px"><div class="icon"></div><h3 class="display">Chef's Specialist</h3><p class="copy">Lorem Ipsum is simply dummy text of the printing and typesetting industry.</p></div>

<!-- About -->
<div class="abs" style="left:110px;top:1130px;width:490px;height:360px;background:linear-gradient(135deg,#5a3a22,#1f1510)" role="img" aria-label="Guests dining together at a candlelit table"></div>
<div class="abs" style="left:133px;top:1115px;width:442px;height:386px;border:2px solid var(--line)"></div>
<div class="rule" style="left:655px;top:1140px;width:80px"></div>
<h2 class="abs display" style="left:655px;top:1158px;font-size:50px">About Us</h2>
<p class="abs copy" style="left:655px;top:1232px;width:430px">Lorem Ipsum is simply dummy text of the printing and typesetting industry. Lorem Ipsum has been the industry's standard dummy text ever since the 1500s, when an unknown printer took a galley of type and scrambled it to make a type specimen book. It has survived not only five centuries, but also the leap into electronic typesetting, remaining essentially unchanged.</p>
<div class="btn" style="left:655px;top:1405px;width:162px;height:45px">Read More</div>

<!-- Specialties -->
<div class="abs" style="left:0;top:1645px;width:1200px;height:505px;background:linear-gradient(90deg,#1f1f1f 0%,#262626 45%,#3a3a3a 70%,#2a2a2a 100%)" role="img" aria-label="Chef plating a garnished dish with tweezers"></div>
<div class="rule" style="left:113px;top:1735px;width:80px"></div>
<h2 class="abs display" style="left:113px;top:1745px;font-size:50px;color:#fff">Our Best Specialties</h2>
<p class="abs copy" style="left:113px;top:1826px;width:460px;color:#fff">Lorem Ipsum is simply dummy text of the printing and typesetting industry. Lorem Ipsum has been the industry's standard dummy text ever since the 1500s, when an unknown printer took a galley of type and scrambled it to make a type specimen book. It has survived not only five centuries, but also the leap into electronic typesetting, remaining essentially unchanged.</p>
<div class="btn" style="left:113px;top:2005px;width:162px;height:45px">View All</div>

<!-- Menu -->
<div class="rule" style="left:560px;top:2222px;width:80px"></div>
<h2 class="abs display" style="left:0;top:2240px;width:1200px;text-align:center;font-size:50px">Explore Our Best Menu</h2>

<div class="abs menu-card" style="left:110px;top:2348px"><div class="menu-img" style="background:linear-gradient(135deg,#b65a2a,#e8d6c2)" role="img" aria-label="Braised chops on a plate"></div><h3 class="display">Braised Chops</h3><p class="copy">Lorem Ipsum is simply dummy text of the<br>printing and typesetting industry.</p><div class="price">$00.00</div></div>
<div class="abs menu-card" style="left:455px;top:2348px"><div class="menu-img" style="background:linear-gradient(135deg,#f2f2f2,#cfcfcf 60%,#4a1a25)" role="img" aria-label="Wine bottle, glass and grapes"></div><h3 class="display">Grapes Wine</h3><p class="copy">Lorem Ipsum is simply dummy text of the<br>printing and typesetting industry.</p><div class="price">$00.00</div></div>
<div class="abs menu-card" style="left:798px;top:2348px"><div class="menu-img" style="background:linear-gradient(135deg,#c8321e,#e08a4a 60%,#6a7d3a)" role="img" aria-label="Chicken with garlic tomatoes in a pan"></div><h3 class="display">Chicken With Garlic Tomatos</h3><p class="copy">Lorem Ipsum is simply dummy text of the<br>printing and typesetting industry.</p><div class="price">$00.00</div></div>

<div class="abs menu-card" style="left:110px;top:2783px"><div class="menu-img" style="background:linear-gradient(180deg,#e2a13a,#5a2f1a 55%,#f0c030)" role="img" aria-label="Double cheese chicken burger"></div><h3 class="display">Doubble Chees Chicken Burger</h3><p class="copy">Lorem Ipsum is simply dummy text of the<br>printing and typesetting industry.</p><div class="price">$00.00</div></div>
<div class="abs menu-card" style="left:455px;top:2783px"><div class="menu-img" style="background:linear-gradient(135deg,#f0d8b0,#c07a3a)" role="img" aria-label="Coconut fried chicken pieces"></div><h3 class="display">Coconut Fried Chicken</h3><p class="copy">Lorem Ipsum is simply dummy text of the<br>printing and typesetting industry.</p><div class="price">$00.00</div></div>
<div class="abs menu-card" style="left:798px;top:2783px"><div class="menu-img" style="background:radial-gradient(ellipse at 50% 50%,#7a6a40,#111 70%)" role="img" aria-label="Glass of white wine on dark background"></div><h3 class="display">Rioja Wine</h3><p class="copy">Lorem Ipsum is simply dummy text of the<br>printing and typesetting industry.</p><div class="price">$00.00</div></div>

<div class="btn" style="left:516px;top:3238px;width:162px;height:45px">View All</div>

<!-- Blog -->
<div class="abs" style="left:0;top:3356px;width:1200px;height:278px;background:linear-gradient(90deg,#3d2a22,#5a3f2e 50%,#2f241d)" role="img" aria-label="Blurred table of food"></div>
<div class="rule" style="left:560px;top:3410px;width:80px"></div>
<h2 class="abs display" style="left:0;top:3440px;width:1200px;text-align:center;font-size:50px;color:#fff">Latest Blog Posts</h2>

<div class="abs blog-card" style="left:112px;top:3545px"><div class="img" style="background:linear-gradient(135deg,#c23a1e,#f0c060)" role="img" aria-label="Pizza slices with melted cheese"></div><div class="meta"><h3 class="display">Blog Title #01</h3><span class="date">12.05.2021</span></div><p class="copy">Lorem Ipsum is simply dummy text of the printing and typesetting industry. Lorem Ipsum has been the industry's standard dummy text ever since the 1500s.</p><a>READ MORE</a></div>
<div class="abs blog-card" style="left:443px;top:3545px"><div class="img" style="background:linear-gradient(135deg,#4f7a2a,#6a1a22 60%,#d0b070)" role="img" aria-label="Red wine glasses outdoors"></div><div class="meta"><h3 class="display">Blog Title #02</h3><span class="date">12.05.2021</span></div><p class="copy">Lorem Ipsum is simply dummy text of the printing and typesetting industry. Lorem Ipsum has been the industry's standard dummy text ever since the 1500s.</p><a>READ MORE</a></div>
<div class="abs blog-card" style="left:775px;top:3545px"><div class="img" style="background:linear-gradient(135deg,#f4f0ea,#c4602a 60%,#7a2a12)" role="img" aria-label="Roasted chicken wings"></div><div class="meta"><h3 class="display">Blog Title #03</h3><span class="date">12.05.2021</span></div><p class="copy">Lorem Ipsum is simply dummy text of the printing and typesetting industry. Lorem Ipsum has been the industry's standard dummy text ever since the 1500s.</p><a>READ MORE</a></div>

<div class="btn" style="left:516px;top:4042px;width:162px;height:45px">View All</div>

<!-- FAQ -->
<div class="rule" style="left:118px;top:4170px;width:80px"></div>
<h2 class="abs display" style="left:115px;top:4185px;font-size:50px">Frequently Ask Questions</h2>
<div class="faq-open"><h4>What types of vehicles can be donated?</h4><p class="copy" style="font-size:12px;line-height:18px;margin-top:6px">Lorem Ipsum is simply dummy text of the printing typesetting the industry's standard dummy text ever since the 1500s.</p></div>
<div class="abs" style="left:560px;top:4312px;width:14px;height:14px;border-radius:50%;background:var(--gold)"></div>
<div class="faq-item" style="top:4410px"><span>Lorem Ipsum is simply text of the printing</span><i class="tick"></i></div>
<div class="faq-item" style="top:4456px"><span>Lorem simply dummy text of the?</span><i class="tick"></i></div>
<div class="faq-item" style="top:4503px"><span>Lorem Ipsum the printing and industry</span><i class="tick"></i></div>
<div class="faq-item" style="top:4550px"><span>Lorem Ipsum is simply industry. Lorem ?</span><i class="tick"></i></div>
<div class="faq-item" style="top:4596px"><span>Lorem and typesetting industry ?</span><i class="tick"></i></div>
<div class="faq-item" style="top:4642px"><span>Lorem and typesetting industry ?</span><i class="tick"></i></div>
<div class="abs" style="left:615px;top:4193px;width:470px;height:455px;background:linear-gradient(135deg,#e9e6df,#dcd8ce)" role="img" aria-label="Street map showing the restaurant location"></div>
<svg class="abs" style="left:870px;top:4380px" width="24" height="34" viewBox="0 0 24 34"><path d="M12 0a12 12 0 0 1 12 12c0 9-12 22-12 22S0 21 0 12A12 12 0 0 1 12 0z" fill="#e04030"/><circle cx="12" cy="12" r="4" fill="#8a1a12"/></svg>

<!-- Newsletter -->
<div class="abs" style="left:0;top:4728px;width:1200px;height:108px;background:var(--amber)"></div>
<h2 class="abs display" style="left:113px;top:4752px;font-size:32px">Newsletter</h2>
<p class="abs copy" style="left:113px;top:4790px;color:#333">Lorem Ipsum is simply dummy text of the printing and typesetting industry.</p>
<div class="field" style="left:635px;top:4767px;width:300px;height:38px;font-size:11px;padding:12px">Email Address</div>
<div class="btn" style="left:943px;top:4767px;width:144px;height:38px">Subscribe</div>

<!-- Footer -->
<footer class="footer">
<div class="abs" style="left:0;top:4836px;width:1200px;height:370px;background:var(--forest)"></div>
<div class="abs" style="left:118px;top:4972px;display:flex;align-items:center;gap:12px"><div style="width:16px;height:16px;border-radius:50%;background:var(--gold)"></div><span style="font-family:'Bebas Neue',sans-serif;font-size:52px;color:var(--gold);letter-spacing:2px">Marlow's</span></div>
<div class="abs" style="left:393px;top:4905px"><h4>Quick Links</h4><ul style="margin-top:14px"><li style="color:var(--gold)"><b>&gt;</b>Home</li><li><b>&gt;</b>About us</li><li><b>&gt;</b>Menu</li><li><b>&gt;</b>FAQs</li><li><b>&gt;</b>Contact us</li></ul></div>
<div class="abs" style="left:572px;top:4905px"><h4>Contact Info</h4><ul style="margin-top:14px"><li><b>&#9990;</b>+(0)1 555-018-42</li><li><b>&#9993;</b>info@marlows.com</li><li>&nbsp;</li><li><b>&#9679;</b>418 Linden Ave.</li><li style="padding-left:22px">Oakridge, CA 94610</li></ul></div>
<div class="abs" style="left:787px;top:4905px"><h4>Contact Us</h4></div>
<div class="field" style="left:788px;top:4970px;width:147px;height:28px">Full Name</div>
<div class="field" style="left:940px;top:4970px;width:147px;height:28px">Phone</div>
<div class="field" style="left:788px;top:5004px;width:299px;height:28px">Email Address</div>
<div class="field" style="left:788px;top:5038px;width:299px;height:52px">Message</div>
<div class="btn" style="left:1000px;top:5096px;width:87px;height:24px">Send</div>
</footer>
<div class="abs" style="left:0;top:5206px;width:1200px;height:53px;background:#fff"></div>
<p class="abs" style="left:113px;top:5225px;font-size:12px;color:#444">Copyright © 2021 Marlow's, All Rights Reserved.</p>
<div class="abs" style="left:943px;top:5218px;display:flex;gap:12px"><div class="social" style="background:var(--gold)"></div><div class="social" style="background:var(--teal)"></div><div class="social" style="background:var(--teal)"></div><div class="social" style="background:var(--teal)"></div></div>

</body>
</html>
```